Welding company needs a business card

We are looking for a logo and business card.

Contact Information for Business Card

418 Cobblestone Lane
York, PA 17402
410-555-0173
Rmfabworksco@quorvamail.com

```html
<!DOCTYPE html>
<html lang="en">
<head>
<meta charset="utf-8">
<title>R&amp;M Fabworks INC. — Business Card</title>
<link href="https://fonts.googleapis.com/css2?family=Della+Respira&family=Ubuntu:wght@400&display=swap" rel="stylesheet">
<style>
  :root {
    --page-bg: #e9e6e2;
    --card-dark: #2a2928;
    --card-mid: #3d3c3a;
    --text-light: #f4f2ee;
    --accent-yellow: #f6e51b;
    --accent-orange: #e85d1f;
    --accent-amber: #f5a623;
  }
  html, body {
    margin: 0;
    padding: 0;
    width: 1200px;
    height: 1000px;
    overflow: hidden;
    background: var(--page-bg);
  }
  .canvas {
    position: relative;
    width: 1200px;
    height: 1000px;
  }
  .business-card {
    position: absolute;
    left: 75px;
    top: 200px;
    width: 1050px;
    height: 600px;
    border-radius: 22px;
    overflow: hidden;
    box-shadow: 0 10px 30px rgba(0,0,0,0.25);
  }
  .workshop-photo {
    position: absolute;
    inset: 0;
    background:
      radial-gradient(ellipse at 55% 55%, var(--card-mid) 0%, var(--card-dark) 70%);
  }
  .card-content {
    position: absolute;
    inset: 0;
    bottom: 92px;
  }
  .brand {
    position: absolute;
    left: 60px;
    right: 60px;
    top: 120px;
    display: flex;
    justify-content: center;
    align-items: center;
    gap: 24px;
  }
  .brand-mark {
    width: 96px;
    height: 96px;
    border-radius: 50%;
    background: var(--accent-amber);
    flex: none;
  }
  .brand-name {
    font-family: "Della Respira", serif;
    font-size: 64px;
    line-height: 1;
    color: var(--text-light);
    letter-spacing: -0.5px;
    white-space: nowrap;
  }
  .contact-list {
    position: absolute;
    left: 0;
    right: 0;
    top: 270px;
    margin: 0;
    padding: 0;
    list-style: none;
    font-family: "Ubuntu", sans-serif;
    font-size: 32px;
    color: var(--text-light);
    text-align: center;
  }
  .contact-item {
    display: flex;
    justify-content: center;
    align-items: center;
    gap: 14px;
    height: 62px;
  }
  .contact-icon {
    width: 30px;
    height: 34px;
    flex: none;
  }
  .accent-band {
    position: absolute;
    left: 0;
    right: 0;
    bottom: 0;
    height: 92px;
    background: linear-gradient(90deg, var(--accent-yellow) 0%, var(--accent-amber) 50%, var(--accent-orange) 100%);
  }
</style>
</head>
<body>
<div class="canvas">
  <div class="business-card">
    <div class="workshop-photo" role="img" aria-label="Dark photo of a welded steel frame in a workshop"></div>
    <div class="card-content">
      <div class="brand">
        <span class="brand-mark"></span>
        <span class="brand-name">R&amp;M Fabworks INC.</span>
      </div>
      <ul class="contact-list">
        <li class="contact-item">
          <svg class="contact-icon" viewBox="0 0 30 34" aria-hidden="true">
            <defs><linearGradient id="pinGrad" x1="0" y1="0" x2="0" y2="1"><stop offset="0" stop-color="#f5a623"/><stop offset="1" stop-color="#f6e51b"/></linearGradient></defs>
            <path d="M15 2C8.4 2 4 6.8 4 12.6 4 20 15 32 15 32s11-12 11-19.4C26 6.8 21.6 2 15 2z" fill="url(#pinGrad)"/>
            <circle cx="15" cy="12.5" r="4.2" fill="#2a2928"/>
          </svg>
          <span>418 Cobblestone Lane, York, PA 17402</span>
        </li>
        <li class="contact-item">
          <svg class="contact-icon" viewBox="0 0 30 34" aria-hidden="true">
            <rect x="8" y="2" width="15" height="29" rx="3" fill="none" stroke="#f39a1f" stroke-width="2.6"/>
            <line x1="13" y1="26" x2="18" y2="26" stroke="#f39a1f" stroke-width="2.4"/>
          </svg>
          <span>410-555-0173</span>
        </li>
        <li class="contact-item">
          <svg class="contact-icon" viewBox="0 0 30 34" aria-hidden="true">
            <rect x="2" y="9" width="26" height="18" fill="#f5a623"/>
            <path d="M2 9l13 10 13-10" fill="none" stroke="#2a2928" stroke-width="2"/>
          </svg>
          <span>Rmfabworksco@quorvamail.com</span>
        </li>
      </ul>
    </div>
    <div class="accent-band"></div>
  </div>
</div>
</body>
</html>
```